Velmorytrips.com web design project + logo design

Hi,

We are a Russian online tour operator - roamquiltex.com

We are looking to tranmsfer our domain to velmorytrips.com. The website and logo need to be velmoryesque - we are not looking to change our functionality, but we need to make the website much more attracitve to clients, much more wild looking but at the same time remaining a professional travel company.

The main concept of the website should be innovative travel (as velmory was an innovator). Alternatively, you could go down the artist route and go down the draw / design your own tour road.

On our website the customer is able to combine travel services (hotels, flights, Visa services, and soon chauffeur, car rental etc...) put it into their basket (the basket definitely has to look better than it is at the moment) and pay for it in one go by card.

We are also stressin our customer support with web chat, call centre etc... (call centre number at the top of the page)

We aim to provide an easy user experience, but we need to make it have some more style, so I will be waiting for what you guys can come up with.
Let me know if you have any questions - skype is: mrkostelin

Industry/Entity Type

It Company

Logo Text

Requirements
Must have
• It is quite a simple task - to take the existing website roamquiltex.com and velmorysize it to create velmorytrips.com, the functionality of the website will remain the same and there are not many pages in the website. Homepage, Checkout step1, Checkout step 2 (you can view both of these if you select a service) and the generic pages for T&C''s, Privacy policy etc...

IMPORTANT UPDATE

We are also looking at how the search results will look in the designs, (please do a search on our website for hotel / flight)

```html
<!DOCTYPE html>
<html lang="ru">
<head>
<meta charset="utf-8">
<title>Отели по направлению — Velmorytrips.com</title>
<link rel="stylesheet" href="https://fonts.googleapis.com/css2?family=PT+Sans:wght@400;700&family=PT+Serif:wght@400&display=swap">
<style>
  :root{
    --paper:#efeadf;
    --paper-dark:#e6dfd0;
    --ink:#2a1a10;
    --text:#1c1c1c;
    --rust:#8a2a0c;
    --rust-light:#9a3414;
    --espresso:#2b120a;
    --grey-star:#6e6e6e;
    --track:#dcdcdc;
    --field:#ece8d8;
    --pin:#b8a868;
    --white:#ffffff;
  }
  *{margin:0;padding:0;box-sizing:border-box}
  html,body{width:1200px;height:843px;overflow:hidden}
  body{
    position:relative;
    background:radial-gradient(ellipse at 50% 40%, #f3efe6 0%, var(--paper) 55%, var(--paper-dark) 100%);
    font-family:"PT Sans",Tahoma,sans-serif;
    color:var(--text);
  }
  .top-band{position:absolute;left:0;top:0;width:1200px;height:4px;background:linear-gradient(90deg,#7a8a78,#a8a890,#6d7d70,#9aa08a)}
  .page-title{position:absolute;left:0;top:25px;width:1200px;text-align:center;font-family:"PT Serif",Georgia,serif;font-weight:400;font-size:19px;letter-spacing:.3px;color:var(--ink)}

  .filters{position:absolute;left:177px;top:70px;width:844px;height:133px;background:var(--white);box-shadow:0 1px 3px rgba(0,0,0,.12)}
  .filter-label{position:absolute;top:33px;font-size:13px;color:var(--ink);white-space:nowrap}
  .filter-stars{position:absolute;left:32px;top:61px;display:flex;gap:4px}
  .price-slider{position:absolute;left:278px;top:60px;width:250px;height:40px}
  .slider-track{position:absolute;left0;left:0;top:7px;width:245px;height:6px;border-radius:3px;background:var(--track)}
  .slider-range{position:absolute;left:37px;top:7px;width:125px;height:6px;background:var(--rust)}
  .slider-handle{position:absolute;top:2px;width:16px;height:16px;border-radius:50%;background:var(--espresso)}
  .slider-scale{position:absolute;top:27px;font-size:10px;color:var(--ink)}
  .name-search{position:absolute;left:601px;top:59px;width:213px;height:38px;background:var(--field);border:1px solid #e4dfcc}

  .hotel{position:absolute;left:177px;width:844px;height:131px;border-bottom:1px dotted #4a3a30}
  .hotel-photo{position:absolute;left:1px;top:0;width:169px;height:94px}
  .photo-night{background:linear-gradient(180deg,#1a3a7a 0%,#3a5aa0 40%,#c8c8c8 60%,#e8d890 80%,#2a3a40 100%)}
  .photo-river{background:linear-gradient(180deg,#8ab0d0 0%,#c8a078 35%,#a06048 55%,#e8e0d0 70%,#6a5a50 100%)}
  .hotel-name{position:absolute;left:183px;top:12px;display:flex;align-items:center;gap:10px;font-family:"PT Serif",Georgia,serif;font-size:16px;color:var(--ink);letter-spacing:.3px}
  .hotel-name .stars{display:flex;gap:5px}
  .hotel-distance{position:absolute;left:183px;top:35px;display:flex;align-items:center;gap:8px;font-size:13.5px;color:#111}
  .hotel-desc{position:absolute;left:185px;top:60px;width:470px;font-family:Arial,"PT Sans",sans-serif;font-size:11px;line-height:13px;color:#111}
  .price-button{position:absolute;left:699px;top:20px;width:149px;height:54px;background:var(--rust);color:#f3e6dc;text-align:center;font-family:"PT Serif",Georgia,serif}
  .price-button .from{display:block;font-size:14px;margin-top:5px}
  .price-button .amount{display:block;font-size:20px;line-height:22px}

  .pagination{position:absolute;left:178px;top:804px;display:flex;gap:3px;font-family:"PT Serif",Georgia,serif;font-size:15px}
  .page-link{height:28px;line-height:28px;background:var(--espresso);color:#f0e6de;text-align:center}
  .page-link.wide{width:169px}
  .page-link.num{width:28px}
  .page-link.current{background:var(--rust-light)}
</style>
</head>
<body>
  <div class="top-band"></div>
  <h1 class="page-title">ОТЕЛИ ПО НАПРАВЛЕНИЮ</h1>

  <section class="filters">
    <span class="filter-label" style="left:32px">Сортировать по: К-ву звезд</span>
    <div class="filter-stars">
      <svg width="90" height="16" viewBox="0 0 90 16">
        <defs><path id="st" d="M8 0.5l2.2 4.9 5.3.5-4 3.6 1.2 5.2L8 12 3.3 14.7l1.2-5.2-4-3.6 5.3-.5z"/></defs>
        <use href="#st" x="0" fill="#8a2a0c"/><use href="#st" x="20" fill="#8a2a0c"/><use href="#st" x="40" fill="#8a2a0c"/>
        <use href="#st" x="60" fill="#6e6e6e"/><use href="#st" x="80" fill="#6e6e6e" transform="translate(-6 0)"/>
      </svg>
    </div>

    <span class="filter-label" style="left:274px">Сортировать по:&nbsp; Ценеза одну ночь(рубли</span>
    <div class="price-slider">
      <div class="slider-track"></div>
      <div class="slider-range"></div>
      <div class="slider-handle" style="left:30px"></div>
      <div class="slider-handle" style="left:155px"></div>
      <span class="slider-scale" style="left:-4px">0</span>
      <span class="slider-scale" style="left:23px">8300</span>
      <span class="slider-scale" style="left:80px">16600</span>
      <span class="slider-scale" style="left:155px">24900</span>
      <span class="slider-scale" style="left:223px">41500</span>
    </div>

    <span class="filter-label" style="left:601px">Найти отель по названию</span>
    <div class="name-search"></div>
  </section>

  <article class="hotel" style="top:270px">
    <div class="hotel-photo photo-night" role="img" aria-label="Фото отеля Verdant вечером"></div>
    <div class="hotel-name">VERDANT <span class="stars"><svg width="56" height="15" viewBox="0 0 56 15" fill="#8a2a0c"><path id="s1" d="M7.5 0.5l2 4.6 5 .4-3.8 3.3 1.1 4.9-4.3-2.6-4.3 2.6 1.1-4.9L.3 5.5l5-.4z"/><use href="#s1" x="20"/><use href="#s1" x="40"/></svg></span></div>
    <div class="hotel-distance"><svg width="14" height="17" viewBox="0 0 14 17"><path d="M7 0a6 6 0 0 0-6 6c0 4.5 6 11 6 11s6-6.5 6-11a6 6 0 0 0-6-6z" fill="#b8a868"/><circle cx="7" cy="6" r="2.3" fill="#efeadf"/></svg>6 км от центра города</div>
    <p class="hotel-desc">Находится в тихом 5-м квартале Праги, на территории парка и поля для игры в гольф. Благодаря хорошо развитой сети общественного транспорта, до центра города и до аэропорта можно доехать на трамвае вс...</p>
    <div class="price-button"><span class="from">Цена от</span><span class="amount">12529 Руб</span></div>
  </article>

  <article class="hotel" style="top:401px">
    <div class="hotel-photo photo-river" role="img" aria-label="Фото отеля-корабля Botel Marevia на реке"></div>
    <div class="hotel-name">BOTEL MAREVIA <span class="stars"><svg width="56" height="15" viewBox="0 0 56 15" fill="#8a2a0c"><use href="#s1"/><use href="#s1" x="20"/><use href="#s1" x="40"/></svg></span></div>
    <div class="hotel-distance"><svg width="14" height="17" viewBox="0 0 14 17"><path d="M7 0a6 6 0 0 0-6 6c0 4.5 6 11 6 11s6-6.5 6-11a6 6 0 0 0-6-6z" fill="#b8a868"/><circle cx="7" cy="6" r="2.3" fill="#efeadf"/></svg>2 км от центра города</div>
    <p class="hotel-desc">Находится на берегу Влтавы, в 5 минутах ходьбы от Карлова Моста и Старого города. ...</p>
    <div class="price-button"><span class="from">Цена от</span><span class="amount">14800 Руб</span></div>
  </article>

  <article class="hotel" style="top:532px">
    <div class="hotel-photo photo-night" role="img" aria-label="Фото отеля Verdant вечером"></div>
    <div class="hotel-name">VERDANT <span class="stars"><svg width="56" height="15" viewBox="0 0 56 15" fill="#8a2a0c"><use href="#s1"/><use href="#s1" x="20"/><use href="#s1" x="40"/></svg></span></div>
    <div class="hotel-distance"><svg width="14" height="17" viewBox="0 0 14 17"><path d="M7 0a6 6 0 0 0-6 6c0 4.5 6 11 6 11s6-6.5 6-11a6 6 0 0 0-6-6z" fill="#b8a868"/><circle cx="7" cy="6" r="2.3" fill="#efeadf"/></svg>6 км от центра города</div>
    <p class="hotel-desc">Находится в тихом 5-м квартале Праги, на территории парка и поля для игры в гольф. Благодаря хорошо развитой сети общественного транспорта, до центра города и до аэропорта можно доехать на трамвае вс...</p>
    <div class="price-button"><span class="from">Цена от</span><span class="amount">12529 Руб</span></div>
  </article>

  <article class="hotel" style="top:663px">
    <div class="hotel-photo photo-river" role="img" aria-label="Фото отеля-корабля Botel Marevia на реке"></div>
    <div class="hotel-name">BOTEL MAREVIA <span class="stars"><svg width="56" height="15" viewBox="0 0 56 15" fill="#8a2a0c"><use href="#s1"/><use href="#s1" x="20"/><use href="#s1" x="40"/></svg></span></div>
    <div class="hotel-distance"><svg width="14" height="17" viewBox="0 0 14 17"><path d="M7 0a6 6 0 0 0-6 6c0 4.5 6 11 6 11s6-6.5 6-11a6 6 0 0 0-6-6z" fill="#b8a868"/><circle cx="7" cy="6" r="2.3" fill="#efeadf"/></svg>2 км от центра города</div>
    <p class="hotel-desc">Находится на берегу Влтавы, в 5 минутах ходьбы от Карлова Моста и Старого города. ...</p>
    <div class="price-button"><span class="from">Цена от</span><span class="amount">14800 Руб</span></div>
  </article>

  <nav class="pagination">
    <span class="page-link wide">Предыдущая страница</span>
    <span class="page-link num current">1</span>
    <span class="page-link num">2</span>
    <span class="page-link num">3</span>
    <span class="page-link num">4</span>
    <span class="page-link num">5</span>
    <span class="page-link wide">Следующая страница</span>
  </nav>
</body>
</html>
```